Human Resource Consulting practice needs a business card design

We need a business card design (double sided colour) for our Human Resource (HR) consulting practice in regional New South Wales, australia. Our business name is Staffwise Partners. We support small and medium business across the Mid North Coast of New South Wales by providing them with outsourced HR support, services and products to help them achieve compliance with workplace legislation and across all areas of the employment lifecycle from recruitment to termination and everything in between. Our corporate colours are hot pink and black. The final design should communicate professionalism, trust, people focus.
I have attached the current (old) business card for your reference.

Target Market(s)

Business owners and high level managers

Industry/Entity Type

Business

Contact Information for Business Card

Name
Title
Phone no
Mobile no
Address
PO Box
email address
website

Colors
e34197

Requirements
Must have
• Tempate for changing business card personal details including Name, position title, mobile number, email address.
• Keep current logo and colours as per attached
• Logo must be presented in 2 colours or black only not white
Nice to have
• One side logo and graphic only other side logo and personal details
Should not have
• Should not be the same as the current version (attached) but a modern interpretation.
• Does not need a busy reverse side with our list of services as per current version. I feel this is too busy.
• No photos

```html
<!DOCTYPE html>
<html lang="en">
<head>
<meta charset="utf-8">
<title>Staffwise Partners – Business Card</title>
<link rel="stylesheet" href="https://fonts.googleapis.com/css2?family=Open+Sans:wght@400;600&display=swap">
<style>
  :root {
    --hot-pink: #e6248f;
    --charcoal: #3a3a3c;
    --ink: #2f2f31;
    --card: #ffffff;
    --card-shade: #ececec;
    --backdrop: #d9d6d1;
  }
  * { box-sizing: border-box; margin: 0; padding: 0; }
  html, body {
    width: 1200px; height: 899px; overflow: hidden;
    background: var(--backdrop);
    font-family: "Open Sans", Arial, sans-serif;
  }
  .business-card {
    position: absolute; left: 75px; top: 150px;
    width: 1050px; height: 600px;
    background: radial-gradient(ellipse at 50% 55%, var(--card) 0%, var(--card) 45%, var(--card-shade) 100%);
    box-shadow: 0 10px 30px rgba(0,0,0,.25);
    overflow: hidden;
  }
  .corner-graphic {
    position: absolute; top: 0; right: 0;
    width: 110px; height: 600px;
    background: linear-gradient(180deg, var(--charcoal) 0%, var(--charcoal) 35%, var(--hot-pink) 100%);
  }
  .brand {
    position: absolute; left: 70px; top: 80px;
    display: flex; align-items: center; gap: 12px;
    font-size: 42px; font-weight: 400; color: var(--ink); letter-spacing: -0.5px;
  }
  .brand-mark { width: 14px; height: 14px; background: var(--hot-pink); }
  .contact-list {
    position: absolute; left: 70px; top: 200px;
    list-style: none; font-size: 21px; line-height: 33px; color: var(--ink);
  }
  .contact-list li { display: flex; align-items: flex-start; gap: 12px; }
  .contact-icon { flex: none; width: 22px; height: 22px; margin-top: 6px; }
  .person {
    position: absolute; right: 150px; bottom: 60px; text-align: right;
  }
  .person-name { font-size: 40px; font-weight: 600; color: var(--hot-pink); line-height: 1.15; }
  .person-title { font-size: 36px; font-weight: 400; color: var(--ink); line-height: 1.2; letter-spacing: 1px; }
</style>
</head>
<body>
  <div class="business-card">
    <div class="corner-graphic" role="img" aria-label="Decorative band area in hot pink and charcoal"></div>

    <div class="brand"><span class="brand-mark"></span>Staffwise Partners</div>

    <ul class="contact-list">
      <li>
        <svg class="contact-icon" viewBox="0 0 22 22"><circle cx="11" cy="11" r="11" fill="var(--hot-pink)"/><path fill="#fff" d="M11 5 L17 10.5 H15.2 V16 H12.4 V12.5 H9.6 V16 H6.8 V10.5 H5 Z"/></svg>
        <span>Suite 14, Harbour Plaza,<br>NSW 2444</span>
      </li>
      <li>
        <svg class="contact-icon" viewBox="0 0 22 22"><circle cx="11" cy="11" r="11" fill="var(--hot-pink)"/><path fill="#fff" d="M7 5.5 L9.3 5 L10.4 8 L9 9.2 Q10.2 11.8 12.8 13 L14 11.6 L17 12.7 L16.5 15 Q10 16 6 8 Z"/></svg>
        <span>02-6583-4120</span>
      </li>
      <li>
        <svg class="contact-icon" viewBox="0 0 22 22"><circle cx="11" cy="11" r="11" fill="var(--hot-pink)"/><rect x="7.5" y="4.5" width="7" height="13" rx="1.3" fill="#fff"/><rect x="8.7" y="6.2" width="4.6" height="7.5" fill="var(--hot-pink)"/></svg>
        <span>0412-558-907</span>
      </li>
      <li>
        <svg class="contact-icon" viewBox="0 0 22 22"><circle cx="11" cy="11" r="11" fill="var(--hot-pink)"/><rect x="5.5" y="9" width="11" height="7" rx="1" fill="#fff"/><rect x="7.5" y="5.5" width="7" height="4" fill="#fff"/></svg>
        <span>02-6583-4121</span>
      </li>
      <li>
        <svg class="contact-icon" viewBox="0 0 22 22"><circle cx="11" cy="11" r="11" fill="var(--hot-pink)"/><rect x="5" y="7" width="12" height="8.5" rx="1" fill="#fff"/><path d="M5.5 7.5 L11 12 L16.5 7.5" fill="none" stroke="var(--hot-pink)" stroke-width="1.2"/></svg>
        <span>daniel@staffwisehr.com.au</span>
      </li>
      <li>
        <svg class="contact-icon" viewBox="0 0 22 22"><circle cx="11" cy="11" r="11" fill="var(--hot-pink)"/><g fill="none" stroke="#fff" stroke-width="1.3"><circle cx="11" cy="11" r="6"/><ellipse cx="11" cy="11" rx="2.6" ry="6"/><path d="M5 11 H17"/></g></svg>
        <span>www.staffwisehr.com.au</span>
      </li>
    </ul>

    <div class="person">
      <p class="person-name">Daniel Hartley</p>
      <p class="person-title">Owner / C.E.O</p>
    </div>
  </div>
</body>
</html>
```